Webdesign Bäckerei Lutz Wendmar
Zielgruppe
Die Bäckerei Wendmar in 09618 Brand-Erbisdorf wünscht einen Relaunch ihrer Website www.baeckerei-wendmar-beispiel.de
Die neue Website soll frisch, modern und einladend für den Nutzer sein. Der Fokus sollte auf dem Sortiment Baguettes, Konditorei, Freiberger Eierschecke, Stollen & Gebäck liegen. Des Weiteren soll es einen Selbstpflegebereich für den Navigationspunkt 'Backstuben-Specials' geben. Dieser Punkt sollte auf der Startseite sichtbar hervorgehoben werden.
Aufgabenstellung
Leider hat die Bäckerei kein Logo, demzufolge nutzen Sie bitte nur den Schriftzug: Bäckerei Lutz Wendmar; Tradition seit 1894

```html
<!DOCTYPE html>
<html lang="de">
<head>
<meta charset="utf-8">
<title>Bäckerei Lutz Wendmar</title>
<link href="https://fonts.googleapis.com/css2?family=Fraunces:opsz,wght@9..144,600;9..144,700&family=Figtree:wght@400;500&display=swap" rel="stylesheet">
<style>
  :root {
    --cream: #fcf6ec;
    --brown: #5b2a0b;
    --header-dark: #4a2410;
    --header-mid: #8a5a34;
    --white: #ffffff;
  }
  * { margin: 0; padding: 0; box-sizing: border-box; }
  html, body { width: 1200px; height: 675px; overflow: hidden; background: var(--cream); }
  body { font-family: "Figtree", sans-serif; position: relative; }

  .site-header {
    position: absolute; top: 0; left: 0; width: 1200px; height: 57px;
    background: linear-gradient(90deg, #7a4a2a 0%, var(--header-mid) 25%, #6b3b1c 50%, var(--header-mid) 75%, var(--header-dark) 100%);
    display: flex; align-items: center; justify-content: space-between;
    padding: 0 37.5px; color: var(--white); z-index: 2;
  }
  .nav { display: flex; gap: 20.5px; font-size: 10.8px; list-style: none; }
  .nav li { display: flex; align-items: center; gap: 5px; }
  .nav .caret { width: 6px; height: 4px; }
  .brand {
    position: absolute; left: 50%; top: 11px; transform: translateX(-50%);
    text-align: center; font-family: "Fraunces", serif; font-weight: 600; line-height: 1;
  }
  .brand .small { display: block; font-size: 12.5px; }
  .brand .large { display: block; font-size: 17px; margin-top: 2px; }

  .categories {
    position: absolute; top: 57px; left: 37.5px;
    display: grid; grid-template-columns: repeat(4, 272px); gap: 12px;
  }
  .category {
    position: relative; height: 337px; overflow: hidden;
  }
  .category .photo { position: absolute; inset: 0; }
  .category::after {
    content: ""; position: absolute; left: 0; right: 0; bottom: 0; height: 45%;
    background: linear-gradient(to bottom, rgba(0,0,0,0), rgba(0,0,0,0.55));
  }
  .category .label {
    position: absolute; left: 20px; top: 280px; transform: translateY(-50%);
    color: var(--white); font-size: 18.5px; font-weight: 500;
    display: flex; align-items: center; gap: 9px; z-index: 1;
  }
  .photo-baguettes { background: linear-gradient(160deg, #8a5a35, #c59a6a 45%, #6b4326); }
  .photo-konditorei { background: radial-gradient(circle at 50% 55%, #5a3420, #1a1414 70%); }
  .photo-stollen { background: linear-gradient(170deg, #e2e0dd, #d8c3a0 55%, #b5a48c); }
  .photo-eierschecke { background: linear-gradient(165deg, #f5f1e8 0%, #f1d27a 40%, #e6b545 65%, #f3dc9a 100%); }

  .history {
    position: absolute; top: 468px; left: 37.5px; width: 820px;
    font-family: "Fraunces", serif; font-weight: 700; color: var(--brown);
    font-size: 52px; line-height: 54px; letter-spacing: 0.2px;
  }
  .intro {
    position: absolute; top: 657px; left: 37.5px;
    font-size: 14px; color: var(--brown); white-space: nowrap;
  }
  .shop-photo {
    position: absolute; top: 622px; left: 606px; width: 556px; height: 60px;
    background: linear-gradient(180deg, #9aa8b4 0%, #3d4146 25%, #2c2f33 100%);
  }
</style>
</head>
<body>
  <header class="site-header">
    <ul class="nav">
      <li>Über Uns <svg class="caret" viewBox="0 0 6 4"><path d="M0 0h6L3 4z" fill="#fff"/></svg></li>
      <li>Unsere Sortimen <svg class="caret" viewBox="0 0 6 4"><path d="M0 0h6L3 4z" fill="#fff"/></svg></li>
      <li>Events</li>
      <li>Kontakt</li>
    </ul>
    <div class="brand"><span class="small">Bäckerei</span><span class="large">Lutz Wendmar</span></div>
    <ul class="nav">
      <li>Baguettes</li>
      <li>Konditorei</li>
      <li>Stollen</li>
      <li>Freiberger Eierschecke</li>
    </ul>
  </header>

  <section class="categories">
    <a class="category">
      <div class="photo photo-baguettes" role="img" aria-label="Frische Baguettes in einem Weidenkorb"></div>
      <span class="label">Baguettes <svg width="25" height="8" viewBox="0 0 25 8"><path d="M0 4h23M19.5 1l3.5 3-3.5 3" stroke="#fff" stroke-width="1.3" fill="none"/></svg></span>
    </a>
    <a class="category">
      <div class="photo photo-konditorei" role="img" aria-label="Gestapelte Schokoladen-Muffins mit Kakaopuder bestäubt"></div>
      <span class="label">Konditorei <svg width="25" height="8" viewBox="0 0 25 8"><path d="M0 4h23M19.5 1l3.5 3-3.5 3" stroke="#fff" stroke-width="1.3" fill="none"/></svg></span>
    </a>
    <a class="category">
      <div class="photo photo-stollen" role="img" aria-label="Angeschnittener Stollen mit Puderzucker auf einem Tuch"></div>
      <span class="label">Stollen &amp; Gebäck <svg width="25" height="8" viewBox="0 0 25 8"><path d="M0 4h23M19.5 1l3.5 3-3.5 3" stroke="#fff" stroke-width="1.3" fill="none"/></svg></span>
    </a>
    <a class="category">
      <div class="photo photo-eierschecke" role="img" aria-label="Nahaufnahme eines Stücks Freiberger Eierschecke"></div>
      <span class="label">Freiberger Eierschecke <svg width="25" height="8" viewBox="0 0 25 8"><path d="M0 4h23M19.5 1l3.5 3-3.5 3" stroke="#fff" stroke-width="1.3" fill="none"/></svg></span>
    </a>
  </section>

  <h1 class="history">Gegründet wurde die Bäckerei 1894 von Gustav Reimann in St.Michaelis</h1>
  <p class="intro">Pretium quam consectetur condimentum eu massa. Et</p>
  <div class="shop-photo" role="img" aria-label="Außenansicht des Bäckereigebäudes mit Ziegeldach"></div>
</body>
</html>
```